AMBER HARBOUR WEB

We need a home design in wordpress, we have now a web but we would like to improve it. Our current web is www.amberharbourvillas.example Our business is holliday rental of villas in Ibiza. Our guest must know that we are a reliable company, professional and with experience and good reviews. We want them to click in our reservation engine: https://bookings.amberharbourvillas.example/en/ and make reservation in our website. We would also like to say that all the properties that we have are just us who commercialize so we have best price available. Many people are going to see our villas in staylodgr.example and look to our website to make a reservation with us so we need to show them that they are at the right place and click at our link to our reservation engine. What make us special is that we are a local company, we are from Ibiza, Our guests are always received in person by the Amber Harbour Villas team. You will enjoy extensive tourist information when you check in and during the entire stay. You will be attended by ChatPelt and calls, always happy to help so that you have a happy and fun stay! Our guest stay is better than in hotel as they have more spece, private swiming pool, private garden, barbeque ... To rent a villa is the best way to stay in Ibiza. We also have a promotional video: https://vidshare.example/Qm7pTz3RxLa Let our philosophy be shown, we think that coming on holiday to Ibiza implies seeing the nature that we have in Ibiza, hence our name AMBER HARBOUR, like the pins that almost touch the sea in Ibiza, or the posidonea meadows where the intense green of the seaweed and the blue of the sea. We are aware of the environment, and we love Ibiza. For us, the client who visits Ibiza, should rent a car, go around the island, eat in a restaurant one day in front of the sea, is a night of partying to the discs, go shopping, visit the ancient heritage of Umanity, make some aquatic sport, enjoy the pool, those are for us Ibiza.

Target Market(s)

Europe, people from Holand, UK, Germany, France, Spain ...

Industry/Entity Type

Tourism

Colors

Designer to choose colors to be used in the design.

Requirements
Must have
• Pictures of Ibiza.
Nice to have
• Our name Amber Harbour Villas is beacuse in Ibiza there is forest that almost touch the watter of the Mediterranean sea, so you can see green of the forest and blue of the sea and the sky. And also beacause under the watter of the sea there is a plant called Posidonia that is also green please see the picture of posidonia.

```html
<!DOCTYPE html>
<html lang="en">
<head>
<meta charset="utf-8">
<title>Amber Harbour Villas – Ibiza</title>
<link href="https://fonts.googleapis.com/css2?family=Marcellus&family=Open+Sans:wght@400;600;700&display=swap" rel="stylesheet">
<style>
:root{
  --green:#8cc63f;
  --green-dark:#6aa51f;
  --blue:#29abe2;
  --blue-dark:#1b7fb8;
  --ink:#333;
  --muted:#8a8a8a;
  --light:#f4f6f7;
  --footer:#262626;
  --white:#fff;
}
*{box-sizing:border-box;margin:0;padding:0}
html,body{width:1200px;height:4484px;overflow:hidden}
body{font-family:"Open Sans",Arial,sans-serif;color:var(--ink);background:var(--white);position:relative}
.abs{position:absolute}
.heading{font-family:"Marcellus",Georgia,serif;font-weight:400;letter-spacing:3px;text-transform:uppercase;text-align:center}
.rule{width:60px;height:3px;background:var(--green);margin:14px auto 0}

/* header */
.site-header{position:absolute;left:0;top:0;width:1200px;height:112px;background:var(--white);display:flex;align-items:center;padding:0 100px;z-index:2}
.brand{display:flex;align-items:center;gap:14px;font-family:"Open Sans",sans-serif;font-weight:700;font-size:22px;color:var(--green-dark);letter-spacing:1px}
.brand-dot{width:34px;height:34px;border-radius:50%;background:var(--green)}
.main-nav{margin-left:auto;display:flex;gap:34px;align-items:center;font-size:14px;font-weight:600;text-transform:uppercase;color:#555}
.btn{display:inline-block;border-radius:40px;color:var(--white);font-weight:700;text-transform:uppercase;font-size:15px;text-align:center}
.btn-book{background:linear-gradient(90deg,var(--green),var(--blue));padding:14px 30px}

/* hero */
.hero{position:absolute;left:0;top:112px;width:1200px;height:668px;background:radial-gradient(ellipse at 60% 10%,#bfe9e6 0%,#4fb8b0 30%,#2f8d6e 60%,#1f6a4a 100%)}
.booking-box{position:absolute;left:260px;top:300px;width:680px;height:300px;background:linear-gradient(135deg,rgba(140,198,63,.85),rgba(41,171,226,.85));padding:30px 50px}
.booking-title{color:var(--white);font-size:34px;letter-spacing:4px;margin-bottom:24px;white-space:nowrap}
.field{background:var(--white);height:46px;border-radius:3px;font-size:14px;color:#777;display:flex;align-items:center;padding:0 16px;justify-content:space-between}
.row{display:flex;gap:16px;margin-top:16px}
.row .field{flex:1}
.btn-hero{background:var(--green);padding:14px 40px;margin:22px auto 0;display:block;width:190px}

/* welcome */
.welcome-title{top:828px;left:0;width:1200px;font-size:40px;color:var(--blue)}
.welcome-title span{color:var(--green)}
.activity{position:absolute;width:260px;text-align:center;font-size:16px;color:#444}
.activity .ico{width:136px;height:136px;border-radius:50%;background:var(--green);margin:0 auto 22px;display:flex;align-items:center;justify-content:center}

/* philosophy */
.philosophy-photo{left:0;top:1460px;width:600px;height:488px;background:linear-gradient(160deg,#6b5a44 0%,#c9b08a 45%,#efe6d4 70%,#5e4c37 100%)}
.philosophy{left:600px;top:1460px;width:600px;height:488px;background:linear-gradient(135deg,var(--green) 0%,#7ec24a 60%,#5fb15a 100%);padding:100px 60px 0;color:var(--white)}
.philosophy h2{text-align:left;font-size:38px;letter-spacing:3px}
.philosophy p{font-size:15px;line-height:26px;margin-top:26px}
.btn-outline{border:2px solid var(--white);padding:14px 40px;margin-top:30px;font-weight:600}

/* testimonials */
.testi-title{top:1990px;left:0;width:1200px;font-size:40px;color:var(--blue)}
.testi-title span{color:var(--green)}
.testimonial{position:absolute;top:2100px;width:260px;text-align:center}
.portrait{width:164px;height:164px;border-radius:50%;margin:0 auto;background:linear-gradient(160deg,#d9c6b2,#9a8472);border:6px solid #eee}
.stars{color:#f6a623;font-size:20px;margin-top:18px;letter-spacing:2px}
.testimonial h3{font-size:16px;font-weight:600;letter-spacing:1px;margin-top:4px;font-family:"Marcellus",serif}
.testimonial p{font-size:13px;line-height:21px;color:var(--muted);margin:8px 10px 0}

/* video */
.video-band{left:0;top:2480px;width:1200px;height:660px;background:linear-gradient(180deg,var(--green) 0%,#7fc26f 15%,#cfe7d6 24%,var(--light) 26%,var(--light) 100%)}
.video-title{top:2520px;left:0;width:1200px;font-size:40px;color:var(--white)}
.video{left:132px;top:2608px;width:932px;height:520px;background:linear-gradient(170deg,#6fa6c4 0%,#a7c7d0 22%,#c7743f 45%,#a8512a 70%,#5c8ea8 100%)}
.play{position:absolute;left:426px;top:220px}

/* properties */
.props-title{top:3166px;left:0;width:1200px;font-size:40px;color:var(--blue)}
.props-title span{color:var(--green)}
.property{position:absolute;top:3248px;width:308px;height:396px;background:var(--white);box-shadow:0 2px 10px rgba(0,0,0,.12);text-align:center}
.property .photo{height:240px}
.property h3{font-family:"Marcellus",serif;font-weight:400;font-size:20px;letter-spacing:2px;margin-top:30px}
.property p{font-size:14px;color:var(--muted);line-height:22px;margin:10px 40px 0}

/* contact */
.contact{left:0;top:3672px;width:1200px;height:456px;background:linear-gradient(180deg,#3aa0d8 0%,#1f86c4 50%,#2b9bd3 100%)}
.contact-title{top:3710px;left:0;width:1200px;font-size:40px;color:var(--white)}
.contact-title .rule{background:var(--white)}
.form{left:340px;top:3796px;width:520px}
.form .input{background:var(--white);height:38px;border-radius:2px;font-size:13px;color:#888;padding:10px 12px}
.form .pair{display:flex;gap:20px;margin-bottom:10px}
.form .pair .input{flex:1}
.form .message{height:108px}
.btn-submit{background:var(--green);width:180px;padding:14px 0;margin:24px auto 0;display:block}

/* footer */
.site-footer{left:0;top:4128px;width:1200px;height:356px;background:var(--footer);color:#bbb}
.info{position:absolute;top:50px;width:300px;text-align:center;font-size:13px;line-height:20px}
.info .ring{width:60px;height:60px;border-radius:50%;background:#3a3a3a;margin:0 auto 14px;display:flex;align-items:center;justify-content:center}
.info h4{color:var(--white);font-size:16px;letter-spacing:1px;font-weight:600;margin-bottom:6px}
.footer-brand{position:absolute;left:120px;top:250px;font-size:22px;color:var(--green)}
.footer-nav{position:absolute;left:640px;top:246px;display:flex;gap:34px;font-size:13px;font-weight:600;color:var(--white);text-transform:uppercase}
.copyright{position:absolute;left:700px;top:292px;font-size:12px;color:#aaa;letter-spacing:1px}
</style>
</head>
<body>

<header class="site-header">
  <div class="brand"><span class="brand-dot"></span>AMBER HARBOUR</div>
  <nav class="main-nav">
    <span>Home</span><span>Experience</span><span>About us</span><span>Contact us</span>
    <a class="btn btn-book">Book now!</a>
  </nav>
</header>

<section class="hero" role="img" aria-label="Underwater photo of green posidonia seagrass meadows in clear blue Ibiza sea"></section>
<div class="booking-box">
  <h1 class="heading booking-title">Amber Harbour Ibiza</h1>
  <div class="field">Best Available Rate <span>▾</span></div>
  <div class="row">
    <div class="field">Check in - Check Out <span>▦</span></div>
    <div class="field">2 Adults - 0 Kids <span>▾</span></div>
  </div>
  <a class="btn btn-hero">Book now</a>
</div>

<h2 class="heading abs welcome-title">Welcome to <span>Amber Harbour</span><div class="rule"></div></h2>

<div class="activity" style="left:80px;top:950px"><div class="ico"><svg width="70" height="60" viewBox="0 0 70 60" fill="none" stroke="#fff" stroke-width="4"><path d="M8 38 L14 18 H56 L62 38 Z"/><rect x="4" y="38" width="62" height="12" rx="3"/><circle cx="18" cy="52" r="5" fill="#fff"/><circle cx="52" cy="52" r="5" fill="#fff"/></svg></div>Should Rent a<br>Car</div>
<div class="activity" style="left:340px;top:950px"><div class="ico"><svg width="70" height="70" viewBox="0 0 70 70" fill="none" stroke="#fff" stroke-width="4"><path d="M35 62 V24"/><path d="M35 24 C25 12 12 14 8 22 M35 24 C45 12 58 14 62 22 M35 24 C30 14 34 6 42 6"/><path d="M10 62 H60"/></svg></div>Go Around The<br>Island</div>
<div class="activity" style="left:600px;top:950px"><div class="ico"><svg width="70" height="60" viewBox="0 0 70 60" fill="none" stroke="#fff" stroke-width="4"><path d="M10 44 A25 25 0 0 1 60 44 Z" fill="#fff"/><circle cx="35" cy="14" r="4" fill="#fff"/><path d="M4 50 H66"/></svg></div>Eat in a Restaurant One Day,<br>in Front of The Sea</div>
<div class="activity" style="left:860px;top:950px"><div class="ico"><svg width="70" height="66" viewBox="0 0 70 66" fill="none" stroke="#fff" stroke-width="4"><path d="M6 32 L35 6 L64 32"/><path d="M14 26 V60 H56 V26"/><path d="M32 50 V32 L44 30 V46"/><circle cx="29" cy="50" r="3" fill="#fff"/><circle cx="41" cy="46" r="3" fill="#fff"/></svg></div>Is A Night Of Partying<br>To The Discos</div>

<div class="activity" style="left:80px;top:1210px"><div class="ico"><svg width="70" height="64" viewBox="0 0 70 64" fill="none" stroke="#fff" stroke-width="4"><path d="M4 8 H14 L22 42 H56 L62 18 H18"/><circle cx="26" cy="54" r="5" fill="#fff"/><circle cx="52" cy="54" r="5" fill="#fff"/></svg></div>Go Shopping</div>
<div class="activity" style="left:340px;top:1210px"><div class="ico"><svg width="60" height="70" viewBox="0 0 60 70" fill="none" stroke="#fff" stroke-width="4"><path d="M20 48 C8 38 8 8 30 6 C52 8 52 38 40 48 Z"/><path d="M22 56 H38 M24 64 H36"/></svg></div>Visit the ancient<br>Heritage of Humanity</div>
<div class="activity" style="left:600px;top:1210px"><div class="ico"><svg width="70" height="70" viewBox="0 0 70 70" fill="none" stroke="#fff" stroke-width="4"><path d="M12 58 L58 12"/><ellipse cx="14" cy="56" rx="5" ry="9" transform="rotate(45 14 56)" fill="#fff"/><ellipse cx="56" cy="14" rx="5" ry="9" transform="rotate(45 56 14)" fill="#fff"/></svg></div>Make Some<br>Aquatic Sport</div>
<div class="activity" style="left:860px;top:1210px"><div class="ico"><svg width="70" height="60" viewBox="0 0 70 60" fill="none" stroke="#fff" stroke-width="4"><circle cx="48" cy="12" r="6" fill="#fff"/><path d="M16 30 L34 18 L42 30"/><path d="M4 42 Q14 34 24 42 T44 42 T66 42"/><path d="M4 54 Q14 46 24 54 T44 54 T66 54"/></svg></div>Enjoy the Pool</div>

<div class="abs philosophy-photo" role="img" aria-label="Photo of an open book on a table in warm light"></div>
<section class="abs philosophy">
  <h2 class="heading">Our Philosophy</h2>
  <p>Amber Harbour Villas is a local company from Ibiza offering hand-picked villas with private pools and gardens. We live close to the pines and the sea, and we share that love for nature with every guest who stays with us.</p>
  <a class="btn btn-outline">Read more</a>
</section>

<h2 class="heading abs testi-title">Our <span>Testimonials</span><div class="rule"></div></h2>
<div class="testimonial" style="left:180px"><div class="portrait" role="img" aria-label="Guest portrait photo"></div><div class="stars">★★★★★</div><h3>LUKE MARTEN</h3><p>We were met in person at the villa and helped all week. The pool and garden were perfect for our family holiday.</p></div>
<div class="testimonial" style="left:470px"><div class="portrait" role="img" aria-label="Guest portrait photo"></div><div class="stars">★★★★★</div><h3>LUKE MARTEN</h3><p>We were met in person at the villa and helped all week. The pool and garden were perfect for our family holiday.</p></div>
<div class="testimonial" style="left:760px"><div class="portrait" role="img" aria-label="Guest portrait photo"></div><div class="stars">★★★★★</div><h3>LUKE MARTEN</h3><p>We were met in person at the villa and helped all week. The pool and garden were perfect for our family holiday.</p></div>

<div class="abs video-band"></div>
<h2 class="heading abs video-title">Our Video<div class="rule" style="background:#fff"></div></h2>
<div class="abs video" role="img" aria-label="Promotional video still of red cliffs over the Ibiza sea">
  <svg class="play" width="80" height="80" viewBox="0 0 80 80"><circle cx="40" cy="40" r="36" fill="rgba(0,0,0,.35)" stroke="#fff" stroke-width="4"/><path d="M32 24 L58 40 L32 56 Z" fill="#fff"/></svg>
</div>

<h2 class="heading abs props-title">Properties <span>List</span><div class="rule"></div></h2>
<div class="property" style="left:112px"><div class="photo" role="img" aria-label="Photo of rocky coast and deep blue sea" style="background:linear-gradient(150deg,#16324a,#2f6f96 50%,#9fc7d8)"></div><h3>PROPERTY 01</h3><p>Sea view villa with private pool and garden.</p></div>
<div class="property" style="left:446px"><div class="photo" role="img" aria-label="Aerial photo of a road through red earth fields" style="background:linear-gradient(150deg,#b0532e,#d98c5f 45%,#6a7a5a)"></div><h3>PROPERTY 02</h3><p>Sea view villa with private pool and garden.</p></div>
<div class="property" style="left:780px"><div class="photo" role="img" aria-label="Photo of sandstone cliffs by the sea" style="background:linear-gradient(150deg,#c98a55,#a45d34 50%,#4d7e9a)"></div><h3>PROPERTY 03</h3><p>Sea view villa with private pool and garden.</p></div>

<section class="abs contact" role="img" aria-label="Photo of turquoise Ibiza sea seen from above"></section>
<h2 class="heading abs contact-title">Contact Us<div class="rule"></div></h2>
<form class="abs form">
  <div class="pair"><div class="input">First Name</div><div class="input">Last Name</div></div>
  <div class="pair"><div class="input">Email</div><div class="input">Phone</div></div>
  <div class="input message">Message</div>
  <a class="btn btn-submit">Submit</a>
</form>

<footer class="abs site-footer">
  <div class="info" style="left:120px"><div class="ring"><svg width="22" height="28" viewBox="0 0 22 28"><path d="M11 1 C5 1 1 5.5 1 11 C1 18 11 27 11 27 S21 18 21 11 C21 5.5 17 1 11 1 Z" fill="#fff"/><circle cx="11" cy="11" r="4" fill="#3a3a3a"/></svg></div><h4>LOCATION</h4>Cala Pinar Road 12,<br>07830 Ibiza, Spain</div>
  <div class="info" style="left:450px"><div class="ring"><svg width="26" height="26" viewBox="0 0 26 26"><path d="M6 2 L10 8 L7 11 C9 15 11 17 15 19 L18 16 L24 20 L21 24 C12 24 2 14 2 5 Z" fill="#fff"/></svg></div><h4>CONTACT</h4>Office: 971 000 123<br>Mob: 600 000 456</div>
  <div class="info" style="left:780px"><div class="ring"><svg width="28" height="20" viewBox="0 0 28 20"><rect x="1" y="1" width="26" height="18" fill="#fff"/><path d="M1 1 L14 11 L27 1" stroke="#3a3a3a" stroke-width="2" fill="none"/></svg></div><h4>EMAIL</h4>info@amberharbourvillas.example<br>www.amberharbourvillas.example</div>
  <div class="footer-brand brand"><span class="brand-dot"></span>AMBER HARBOUR</div>
  <nav class="footer-nav"><span>Home</span><span>Experience</span><span>About us</span><span>Contact us</span></nav>
  <div class="copyright">© Copyright 2019 Amber Harbour. All rights reserved</div>
</footer>

</body>
</html>
```